Physiotherapy Referral Pad

-Need a referral pad for physiotherapy to be provided to doctors' offices. I would like it to be simple, not too cluttered and sharp looking so doctors can quickly complete it for clients.

-I have attached my logo which I would like to include. I have also included my business cards to keep the style, font, colors etc consistent.

-I would like to include my slogan
From Our Home To Yours

-I would like it to include services options with tick boxes for Mobile, Clinic, Telehealth, NPKRTW

-I would like for it to say Call to Book or Book Online

-I would like it to include my clinic address:
742 Larkin Crescent
Whitehorse, YT
Y1B2K9

-I would like it to include my contact info:
Gavin Trusk BSc(kin), MPT, CAFCI, IMS
(867)555-0142
physio@trusktherapy.ca

-I would like lines for the following:
Patient Name:
Diagnosis/Recommendations:
(extra lines to fill out patient info)

Physician Signature
Date

Target Market(s)

Physicians to refer clients to physiotherapy

Industry/Entity Type

Physical Therapy

Requirements
Must have
• Clean, concise, easy to look at and find pertinant categories for physicians
Nice to have
• Trusk Therapy color scheme. Please see business cards and website as needed
Should not have
• Not too cluttered or wordy

```html
<!DOCTYPE html>
<html lang="en">
<head>
<meta charset="utf-8">
<title>Trusk Therapy – Referral Pad</title>
<link href="https://fonts.googleapis.com/css2?family=Lato:wght@400;700;900&display=swap" rel="stylesheet">
<style>
  :root{
    --green:#0d5048;
    --navy:#2c4372;
    --panel:#f2f2f4;
    --paper:#ffffff;
    --backdrop:#d6d6d6;
  }
  *{margin:0;padding:0;box-sizing:border-box;}
  html,body{width:1056px;height:1200px;overflow:hidden;background:var(--backdrop);}
  body{font-family:'Lato',sans-serif;color:var(--green);}
  .pad{position:absolute;left:104px;top:0;width:848px;height:1200px;background:var(--paper);overflow:hidden;}
  .side-panel{position:absolute;left:21px;top:0;width:257px;height:1137px;background:var(--panel);}

  .brand{position:absolute;left:21px;top:120px;width:257px;display:flex;flex-direction:column;align-items:center;}
  .brand-mark{width:40px;height:40px;border-radius:50%;background:var(--navy);margin-bottom:16px;}
  .brand-name{font-weight:700;font-size:32px;line-height:1.15;color:var(--green);text-align:center;}
  .slogan{margin-top:14px;font-size:16px;color:var(--navy);text-align:center;}

  .booking{position:absolute;left:21px;top:900px;width:257px;text-align:center;font-size:17px;line-height:24px;color:var(--green);font-weight:700;}

  .header{position:absolute;right:55px;top:48px;text-align:right;}
  .header .name{font-weight:900;font-size:38px;color:var(--green);letter-spacing:.3px;line-height:1.1;}
  .header .credentials{font-size:21px;color:var(--navy);margin-top:4px;}
  .header .address{font-size:16px;color:var(--navy);line-height:20px;margin-top:9px;}
  .contact{list-style:none;margin-top:8px;}
  .contact li{font-size:16px;color:var(--navy);line-height:22px;display:flex;justify-content:flex-end;align-items:center;gap:12px;}
  .contact svg{width:15px;height:15px;flex:none;}
  .header-rule{position:absolute;left:277px;top:265px;width:516px;height:2px;background:var(--navy);}

  .field{position:absolute;left:299px;right:55px;display:flex;align-items:flex-end;font-size:24px;color:var(--green);}
  .fill{flex:1;border-bottom:2.5px dotted var(--green);margin-left:8px;margin-bottom:6px;}
  .gender{position:absolute;left:299px;top:362px;display:flex;align-items:center;font-size:24px;}
  .option{display:flex;align-items:center;font-size:18px;margin-left:26px;}
  .option .box{width:15px;height:15px;border:1.6px solid var(--green);margin-right:14px;}
  .option + .option{margin-left:30px;}
  .line{position:absolute;left:299px;width:492px;border-bottom:2.5px dotted var(--green);}

  .date-label{position:absolute;left:21px;width:257px;top:1013px;text-align:center;font-size:23px;color:var(--navy);}
  .date-line{position:absolute;left:57px;width:184px;top:1083px;border-bottom:2.5px dotted var(--green);}
  .sign-line{position:absolute;left:606px;width:185px;top:1048px;border-bottom:2.5px dotted var(--green);}
  .sign-label{position:absolute;right:57px;top:1062px;font-size:24px;color:var(--green);}

  .footer-rule{position:absolute;left:0;width:848px;height:2px;background:var(--green);}
  .services{position:absolute;left:0;top:1144px;width:848px;height:33px;background:var(--green);color:#fff;display:flex;justify-content:center;align-items:center;font-size:17px;letter-spacing:2px;}
  .service{display:flex;align-items:center;}
  .service .tick{width:12px;height:12px;border:1.5px solid #fff;margin-right:9px;}
  .services .sep{margin:0 22px;}
</style>
</head>
<body>
  <main class="pad">
    <div class="side-panel"></div>

    <div class="brand">
      <span class="brand-mark"></span>
      <div class="brand-name">Trusk<br>Therapy</div>
      <div class="slogan">From Our Home To Yours</div>
    </div>

    <div class="booking">Call to Book<br>or Book Online</div>

    <header class="header">
      <div class="name">GAVIN TRUSK</div>
      <div class="credentials">BSc(kin), MPT, CAFCI, IMS</div>
      <div class="address">742 Larkin Crescent<br>Whitehorse, YT Y1B2K9</div>
      <ul class="contact">
        <li>(867)555-0142
          <svg viewBox="0 0 24 24"><path fill="#0d5048" d="M6.6 10.8a15 15 0 0 0 6.6 6.6l2.2-2.2c.3-.3.7-.4 1-.2 1.1.4 2.3.6 3.6.6.6 0 1 .4 1 1V20c0 .6-.4 1-1 1A17 17 0 0 1 3 4c0-.6.4-1 1-1h3.5c.6 0 1 .4 1 1 0 1.3.2 2.5.6 3.6.1.3 0 .7-.2 1z"/></svg>
        </li>
        <li>physio@trusktherapy.ca
          <svg viewBox="0 0 24 24"><rect x="2" y="5" width="20" height="14" fill="#0d5048"/><path d="M2 5l10 8 10-8M2 19l8-7M22 19l-8-7" stroke="#fff" stroke-width="1.6" fill="none"/></svg>
        </li>
        <li>www.trusktherapy.ca
          <svg viewBox="0 0 24 24" fill="none" stroke="#0d5048" stroke-width="1.6"><circle cx="12" cy="12" r="10"/><ellipse cx="12" cy="12" rx="4.5" ry="10"/><path d="M2 12h20M4 7h16M4 17h16"/></svg>
        </li>
      </ul>
    </header>

    <div class="header-rule"></div>

    <div class="field" style="top:312px;">Patient Name:<span class="fill"></span></div>

    <div class="gender">Gender:
      <span class="option"><span class="box"></span>Male</span>
      <span class="option"><span class="box"></span>Female</span>
    </div>

    <div class="field" style="top:462px;">Diagnosis:<span class="fill"></span></div>
    <div class="line" style="top:533px;"></div>
    <div class="line" style="top:582px;"></div>
    <div class="line" style="top:630px;"></div>
    <div class="line" style="top:679px;"></div>
    <div class="line" style="top:727px;"></div>

    <div class="date-label">Date:</div>
    <div class="date-line"></div>

    <div class="sign-line"></div>
    <div class="sign-label">(Signature)</div>

    <div class="footer-rule" style="top:1136px;"></div>
    <footer class="services">
      <span class="service"><span class="tick"></span>Mobile</span><span class="sep">|</span>
      <span class="service"><span class="tick"></span>Clinic</span><span class="sep">|</span>
      <span class="service"><span class="tick"></span>Telehealth</span><span class="sep">|</span>
      <span class="service"><span class="tick"></span>NPKRTW</span>
    </footer>
    <div class="footer-rule" style="top:1181px;"></div>
  </main>
</body>
</html>
```